Stationery Required - Own Logo provided

Hi,

We are a retail company called 'Copperfinch Trading Limited' based in the UK and would like some corporate stationery designed.

We have provided our Logo which we would like to use (Its attached to this brief)...

The designs must be orginal, professional, stylish and interesting!

Target Market(s)

We will use this stationery to communicate with our wholesale suppliers and employees, so it must have a 'professional' feel about it.

Industry/Entity Type

It Company

Requirements
Must have
• Must be professional, corporate, stylish and not to 'fussy'. we require ... Business card design, a4 letter, compliment slip. All designs must be supplied in a format where the text (address/telephone numbers etc..) can be edited, as we have alot of staff and operate out of several different premises.
Nice to have
• I would like a windows backround picture file supplied as well so we can integrate that onto our computer systems.

```html
<!DOCTYPE html>
<html lang="en">
<head>
<meta charset="utf-8">
<title>Copperfinch Trading Limited – Stationery</title>
<link rel="stylesheet" href="https://fonts.googleapis.com/css2?family=Arimo:wght@400;700&family=Italianno&display=swap">
<style>
  :root{
    --bg:#ece9e4;
    --paper:#ffffff;
    --green-deep:#3b5f26;
    --green-dark:#4f7a33;
    --green:#7cb342;
    --green-light:#a8d064;
    --green-pale:#d7ecb0;
    --ink:#1e1e1e;
    --muted:#555;
  }
  *{box-sizing:border-box;margin:0;padding:0}
  html,body{width:1200px;height:900px;overflow:hidden}
  body{position:relative;background:var(--bg);font-family:"Arimo",Arial,sans-serif;color:var(--ink)}
  .piece{position:absolute;overflow:hidden;box-shadow:0 1px 3px rgba(0,0,0,.25)}
  .brand{font-family:"Arimo",Arial,sans-serif;font-weight:700;color:var(--green-dark);line-height:1.05;display:flex;align-items:center;gap:8px}
  .brand .dot{width:12px;height:12px;background:var(--green-dark);flex:none}
  .contact{font-size:8px;font-weight:700;line-height:1.2;color:var(--ink)}
  .contact b{color:var(--green)}
  .rule-v{position:absolute;width:3px;background:var(--green-deep)}
  .person{font-family:"Italianno",cursive;color:var(--green);line-height:1}
  .role{font-size:7px;color:var(--muted)}
  .fill{position:absolute;inset:0}

  /* Letterhead */
  .letterhead{left:40px;top:22px;width:436px;height:636px;background:var(--paper)}
  .letterhead__head{position:absolute;inset:0 0 auto 0;height:110px}
  .letterhead__brand{position:absolute;left:32px;top:44px;font-size:17px}
  .letterhead__rule{left:242px;top:36px;height:58px}
  .letterhead__contact{position:absolute;left:252px;top:34px}
  .letterhead__foot{position:absolute;left:0;right:0;top:102px;height:4px;background:var(--green-deep)}

  /* Wallpaper panels */
  .wall{left:385px;width:258px;height:153px}
  .wall--wave{top:152px;background:linear-gradient(180deg,var(--green-light),var(--green) 55%,var(--green-dark))}
  .wall--glow{top:309px;background:radial-gradient(ellipse at 45% 50%,var(--green-light),var(--green) 45%,var(--green-deep))}
  .wall__brand{position:absolute;left:68px;top:58px;font-size:19px;color:var(--green-deep)}
  .wall__brand .dot{background:var(--green-deep)}

  /* Large business card */
  .card-lg{left:728px;top:18px;width:452px;height:252px;background:linear-gradient(180deg,var(--green-dark),var(--green) 60%,var(--green-dark))}
  .card-lg__top{position:absolute;inset:0 0 auto 0;height:90px;background:linear-gradient(90deg,#e9efe3,#fff 35%,#fff 60%,var(--green-light))}
  .card-lg__brand{position:absolute;left:118px;top:30px;font-size:24px}
  .card-lg__name{position:absolute;left:166px;top:148px;font-size:34px;color:#fff}
  .card-lg__role{position:absolute;left:182px;top:180px;font-size:11px;font-weight:700;color:var(--green-pale)}
  .card-lg__line{position:absolute;left:100px;top:196px;width:328px;height:2px;background:var(--green-pale)}
  .card-lg__addr{position:absolute;left:4px;top:208px;font-size:10px;font-weight:700;color:#fff;line-height:1.5}
  .card-lg__contact{position:absolute;right:4px;top:214px;font-size:10px;font-weight:700;color:#fff;line-height:1.25}
  .card-lg__contact b{color:var(--green-pale)}

  /* Small business cards */
  .card{left:12px;width:270px;height:142px;background:var(--paper)}
  .card--a{top:441px}
  .card--b{top:598px}
  .card--back{top:748px;background:linear-gradient(180deg,var(--green-light),#fff 30%,#fff 70%,var(--green-dark))}
  .card__name{position:absolute;left:34px;top:40px;font-size:22px}
  .card__role{position:absolute;left:46px;top:60px}
  .card__rule{left:150px;top:22px;height:96px;width:2px}
  .card__contact{position:absolute;left:160px;top:40px;font-size:6.5px;font-weight:400}
  .card__brand{position:absolute;left:6px;top:106px;font-size:10px}
  .card__brand .dot{width:8px;height:8px}
  .card-back__brand{position:absolute;left:58px;top:40px;font-size:17px}
  .card-back__web{position:absolute;left:0;right:0;top:84px;text-align:center;font-size:10px;font-weight:700}

  .label{position:absolute;font-weight:700;font-size:24px;letter-spacing:3px;color:#000}

  /* Envelope */
  .envelope{left:623px;top:552px;width:564px;height:246px;overflow:visible;box-shadow:none}
  .envelope__window{position:absolute;left:20px;top:154px;width:274px;height:84px;border-radius:10px;background:linear-gradient(180deg,#d8d8d8,#fff 50%,#d8d8d8);border:1px solid #bbb}

  /* Compliment slip */
  .slip{left:623px;top:798px;width:564px;height:100px;background:var(--paper);box-shadow:none}
  .slip__brand{position:absolute;left:48px;top:42px;font-size:18px}
  .slip__rule{left:360px;top:32px;height:60px}
  .slip__contact{position:absolute;left:370px;top:32px;font-size:7.5px;line-height:1.15}
</style>
</head>
<body>

<!-- Letterhead -->
<section class="piece letterhead" aria-label="A4 letterhead">
  <svg class="letterhead__head" viewBox="0 0 436 110" preserveAspectRatio="none" aria-hidden="true">
    <defs>
      <linearGradient id="lhTop" x1="0" x2="1"><stop offset="0" stop-color="#4f7a33"/><stop offset=".35" stop-color="#fff"/><stop offset="1" stop-color="#4f7a33"/></linearGradient>
    </defs>
    <rect width="436" height="110" fill="#fff"/>
    <rect width="436" height="22" fill="url(#lhTop)"/>
    <path d="M300 0H436V102H420V40Q420 22 390 22H300Z" fill="#3b5f26"/>
    <path d="M380 22Q412 24 412 50V102H402V52Q402 30 372 26Z" fill="#7cb342"/>
    <path d="M0 96H436V100H0Z" fill="#a8d064"/>
  </svg>
  <div class="brand letterhead__brand"><span class="dot"></span><span>Copperfinch<br>Trading Limited</span></div>
  <span class="rule-v letterhead__rule"></span>
  <div class="contact letterhead__contact">
    17 Mill Lane<br>Ashbrook<br>County Down<br>BT30 4QP<br>
    <b>Tel:</b> 07700900418<br><b>Email:</b> hello@copperfinch.co.uk<br>www.copperfinch.co.uk
  </div>
  <span class="letterhead__foot"></span>
</section>

<!-- Desktop wallpaper, wave -->
<section class="piece wall wall--wave" aria-label="Desktop wallpaper with waves">
  <svg class="fill" width="258" height="153" viewBox="0 0 258 153" aria-hidden="true">
    <path d="M0 40Q70 10 130 40T258 30V60Q190 80 130 60T0 70Z" fill="#d7ecb0" opacity=".55"/>
    <path d="M0 60Q80 30 140 62T258 50V90Q190 110 130 90T0 100Z" fill="#e6f3cc" opacity=".6"/>
    <path d="M0 120Q90 96 258 112V153H0Z" fill="#4f7a33"/>
  </svg>
  <div class="brand wall__brand"><span class="dot"></span><span>Copperfinch<br>Trading Limited</span></div>
</section>

<!-- Desktop wallpaper, glow -->
<section class="piece wall wall--glow" aria-label="Desktop wallpaper">
  <div class="brand wall__brand"><span class="dot"></span><span>Copperfinch<br>Trading Limited</span></div>
</section>

<!-- Large business card -->
<section class="piece card-lg" aria-label="Business card">
  <div class="card-lg__top"></div>
  <div class="brand card-lg__brand"><span class="dot"></span><span>Copperfinch<br>Trading Limited</span></div>
  <p class="person card-lg__name">Martin Hale</p>
  <p class="card-lg__role">Company Director</p>
  <span class="card-lg__line"></span>
  <p class="card-lg__addr">17 Mill Lane<br>Ashbrook, County Down<br>BT30 4QP</p>
  <p class="card-lg__contact"><b>Tel:</b> 07700900418<br><b>Email:</b> hello@copperfinch.co.uk<br>www.copperfinch.co.uk</p>
</section>

<!-- Small card, front A -->
<section class="piece card card--a" aria-label="Business card front">
  <svg class="fill" width="270" height="142" viewBox="0 0 270 142" aria-hidden="true">
    <rect width="270" height="10" fill="#4f7a33" opacity=".8"/>
    <path d="M236 10Q262 12 262 40V128H270V10Z" fill="#7cb342"/>
    <path d="M0 84Q70 70 140 104T270 118V142H0Z" fill="#3b5f26"/>
    <path d="M0 92Q70 80 140 110T270 126V142H0Z" fill="#8fc24d"/>
    <rect y="134" width="270" height="8" fill="#4f7a33"/>
  </svg>
  <p class="person card__name">Martin Hale</p>
  <p class="role card__role">Company Director</p>
  <span class="rule-v card__rule"></span>
  <p class="contact card__contact">17 Mill Lane<br>Ashbrook<br>County Down<br>BT30 4QP<br><b>Tel:</b> 07700900418<br><b>Email:</b> hello@copperfinch.co.uk<br>www.copperfinch.co.uk</p>
</section>
<p class="label" style="left:290px;top:504px">Front</p>

<!-- Small card, front B -->
<section class="piece card card--b" aria-label="Business card front">
  <svg class="fill" width="270" height="142" viewBox="0 0 270 142" aria-hidden="true">
    <rect width="270" height="10" fill="#4f7a33" opacity=".8"/>
    <path d="M226 10Q258 12 258 46V142H270V10Z" fill="#7cb342"/>
    <path d="M0 130H200Q240 130 258 110V142H0Z" fill="#4f7a33"/>
  </svg>
  <p class="person card__name">Martin Hale</p>
  <p class="role card__role">Company Director</p>
  <span class="rule-v card__rule"></span>
  <p class="contact card__contact">17 Mill Lane<br>Ashbrook<br>County Down<br>BT30 4QP<br><b>Tel:</b> 07700900418<br><b>Email:</b> hello@copperfinch.co.uk<br>www.copperfinch.co.uk</p>
  <div class="brand card__brand"><span class="dot"></span><span>Copperfinch Trading Limited</span></div>
</section>
<p class="label" style="left:288px;top:671px">Front</p>

<!-- Small card, back -->
<section class="piece card card--back" aria-label="Business card back">
  <div class="brand card-back__brand"><span class="dot"></span><span>Copperfinch<br>Trading Limited</span></div>
  <p class="card-back__web">www.copperfinch.co.uk</p>
</section>
<p class="label" style="left:294px;top:831px">Back</p>

<!-- Envelope -->
<section class="piece envelope" aria-label="Window envelope">
  <svg class="fill" width="564" height="246" viewBox="0 0 564 246" aria-hidden="true">
    <polygon points="0,74 282,0 564,74 564,246 0,246" fill="#fff"/>
    <line x1="0" y1="74" x2="564" y2="74" stroke="#e2e2e2"/>
  </svg>
  <div class="envelope__window"></div>
</section>

<!-- Compliment slip -->
<section class="piece slip" aria-label="Compliment slip">
  <svg class="fill" width="564" height="100" viewBox="0 0 564 100" aria-hidden="true">
    <defs>
      <linearGradient id="slipBand" x1="0" x2="1"><stop offset="0" stop-color="#4f7a33"/><stop offset=".3" stop-color="#fff"/><stop offset=".55" stop-color="#fff"/><stop offset="1" stop-color="#3b5f26"/></linearGradient>
    </defs>
    <rect width="564" height="100" fill="url(#slipBand)"/>
    <path d="M350 16H520Q548 16 548 44V94H564V0H350Z" fill="#3b5f26"/>
    <path d="M500 16Q538 18 540 50V94H530V52Q528 26 494 20Z" fill="#7cb342"/>
    <rect x="350" y="16" width="170" height="78" rx="14" fill="#fff"/>
    <rect y="93" width="564" height="4" fill="#3b5f26"/>
  </svg>
  <div class="brand slip__brand"><span class="dot"></span><span>Copperfinch<br>Trading Limited</span></div>
  <span class="rule-v slip__rule"></span>
  <p class="contact slip__contact">17 Mill Lane<br>Ashbrook<br>County Down<br>BT30 4QP<br><b>Tel:</b> 07700900418<br><b>Email:</b> hello@copperfinch.co.uk<br>www.copperfinch.co.uk</p>
</section>

</body>
</html>
```